We need a MODERN credit application banner

We have a program that helps people get pre-qualified for an auto loan. Our current Application page/Success page is dated and does not have the colors we want. I want to use fonts and colors that match our partner CrestLedger (www.crestledger-demo.com). I want to include their powered by logo, tallymark rating logo, and swift4lending logo all in a matching CrestLedger Color scheme. I also need a Favicon that matches your design for the page. I attached our deck so you can get more content. To be clear the application page and success pages below are the targets of this redesign! You can visit www.pbelvoiradvertising-demo.com to get more information from our website or www.swift4lending-demo.com.

Target Market(s)

Car dealers and their consumers

Industry/Entity Type

Automotive

Requirements
Must have
• It must offer the same data that is on the existing art
Nice to have
• Looking for a Clean but Interesting design.
Should not have
• No red and black. Do not change the form fills.

```html
<!DOCTYPE html>
<html lang="en">
<head>
<meta charset="utf-8">
<title>swift4lending – Pre-Qualification Success</title>
<link href="https://fonts.googleapis.com/css2?family=Montserrat:ital,wght@0,400;0,500;0,600;0,700;0,800;0,900;1,500;1,700;1,800&display=swap" rel="stylesheet">
<style>
:root{
  --sky:#e3f8fd;
  --white:#ffffff;
  --brand:#0aa6cd;
  --brand-light:#43e5fd;
  --teal-deep:#005469;
  --teal-dark:#00495c;
  --yellow:#fcd600;
  --ink:#0f2b33;
  --olive-dark:#2e2a05;
  --olive:#8d7c0c;
  --gold:#c9ac12;
  --gauge-pale:#d3ecf3;
}
*{margin:0;padding:0;box-sizing:border-box}
html,body{width:844px;height:1200px;overflow:hidden}
body{background:var(--sky);font-family:"Montserrat",sans-serif;position:relative;color:var(--white)}
.page{position:absolute;left:48px;top:37px;width:748px;height:1119px;background:var(--white);overflow:hidden;box-shadow:0 0 6px rgba(0,0,0,.12)}
.abs{position:absolute}
.brand-name{font-family:"Montserrat",sans-serif;font-weight:800;color:var(--brand);letter-spacing:-.5px;white-space:nowrap}
.header-logo{left:0;width:748px;top:16px;text-align:center;font-size:22px}
.rule-yellow{left:0;top:68px;width:748px;height:4px;background:var(--yellow)}
.hero{left:0;top:72px;width:748px;height:282px;background:linear-gradient(100deg,#6b5c0a 0%,var(--gold) 22%,var(--olive) 34%,var(--olive-dark) 44%,#3a3306 58%,var(--gold) 72%,#a8930f 86%,var(--olive) 100%)}
.hero-check{left:326px;top:100px}
.hero-title{left:0;width:748px;top:212px;text-align:center;font-weight:900;font-size:48px;letter-spacing:1px;color:var(--white)}
.hero-frame{left:127px;top:269px;width:493px;height:42px;border:1px solid var(--yellow);padding:4px}
.hero-frame-inner{width:100%;height:100%;border:1.5px solid var(--yellow);display:flex;align-items:center;justify-content:center;font-weight:700;font-size:11px;letter-spacing:1.5px;color:var(--white);white-space:nowrap}
.rule-dark{left:0;top:352px;width:748px;height:3px;background:#163d18}
.panel{left:0;top:355px;width:748px;height:739px;background:var(--teal-deep)}
.amount-tab{left:239px;top:372px;width:448px;height:40px;background:var(--yellow);border-radius:26px 26px 0 0;display:flex;align-items:center;justify-content:center;font-style:italic;font-weight:800;font-size:15px;letter-spacing:2.4px;color:var(--teal-dark);white-space:nowrap}
.congrats-box{left:59px;top:408px;width:629px;height:157px;border:4px solid var(--white);border-radius:0 0 40px 40px;background:radial-gradient(ellipse at 50% 0%,var(--brand-light) 0%,#1ec3e6 35%,var(--brand) 80%);box-shadow:0 6px 12px rgba(0,0,0,.25);text-align:center}
.congrats-title{margin-top:38px;font-weight:800;font-size:33px;letter-spacing:3.5px;text-shadow:0 2px 5px rgba(0,0,0,.25)}
.congrats-sub{margin-top:7px;font-weight:500;font-size:22px;text-shadow:0 2px 4px rgba(0,0,0,.2)}
.congrats-sub strong{font-weight:700}
.badge{left:32px;top:368px}
.dealer-note{left:63px;top:592px;font-style:italic;font-weight:500;font-size:14.5px;letter-spacing:1.1px;white-space:nowrap}
.step-lead{left:63px;top:636px;font-weight:800;font-size:26px;letter-spacing:-.5px;white-space:nowrap}
.step-lead span{color:var(--yellow)}
.step-title{left:61px;top:666px;font-weight:900;font-size:57px;letter-spacing:-1px;color:var(--yellow);line-height:1;white-space:nowrap}
.step-list{left:62px;top:748px;list-style:none;font-style:italic;font-weight:500;font-size:16px;letter-spacing:1.4px;line-height:25.5px}
.step-list li{display:flex;white-space:nowrap}
.step-list .num{width:22px;flex:none}
.step-list u{text-underline-offset:3px}
.btn{top:879px;height:34px;width:155px;background:var(--yellow);border-radius:17px;display:flex;align-items:center;justify-content:center;gap:7px;color:var(--ink);font-weight:700;font-size:9.5px;letter-spacing:1px;box-shadow:0 3px 5px rgba(0,0,0,.3);white-space:nowrap}
.btn-print{left:62px}
.btn-map{left:264px}
.limited{left:62px;top:944px;width:358px;text-align:center;font-weight:700;font-size:10.6px;letter-spacing:.6px;white-space:nowrap}
.act-now{left:62px;top:962px;width:358px;text-align:center;font-weight:900;font-size:36px;color:var(--yellow);white-space:nowrap}
.score-pill{left:441px;top:646px;width:140px;height:84px;background:var(--brand);border-radius:42px;padding:15px 0 0 12px}
.score-num{width:78px;text-align:center;font-weight:900;font-size:28px;line-height:1;letter-spacing:-1px}
.score-label{width:86px;text-align:center;font-weight:600;font-size:8.4px;line-height:10px;margin-top:4px}
.rating-pill{left:488px;top:739px;width:96px;height:34px;background:var(--brand);border-radius:17px;display:flex;align-items:center;padding-left:11px;font-weight:700;font-size:6.5px;color:var(--white);white-space:nowrap}
.gauge{left:530px;top:604px}
.fineprint{left:455px;top:806px;width:250px;font-size:7.2px;line-height:12px;color:var(--white)}
.fineprint p{position:relative;padding-left:14px;margin-bottom:12px}
.fineprint p::before{content:"*";position:absolute;left:0;top:-1px}
.footer{left:0;top:1057px;width:748px;height:62px;background:var(--white)}
.chat{left:50px;top:1022px;width:59px;height:57px;background:var(--white);border-radius:8px 8px 14px 14px;padding:3px 3px 5px}
.chat-inner{width:100%;height:100%;background:var(--brand);border-radius:6px 6px 10px 10px;display:flex;flex-direction:column;align-items:center;padding-top:5px;font-weight:800;font-size:7px;letter-spacing:.8px}
.chat-inner svg{margin-bottom:4px}
.chat-inner span{color:var(--white)}
.footer-swift{left:365px;top:1082px;font-size:16px}
.footer-powered{left:506px;top:1074px;font-size:6.5px;letter-spacing:1.2px;color:var(--brand);font-weight:500;white-space:nowrap}
.footer-crest{left:506px;top:1082px;font-size:16px;font-weight:500}
.footer-tally{left:646px;top:1086px;font-size:9px;font-weight:600;display:flex;align-items:center;gap:4px}
.footer-tally i{display:inline-block;width:9px;height:9px;background:var(--brand)}
</style>
</head>
<body>
<main class="page">
  <div class="abs brand-name header-logo">swift4lending</div>
  <div class="abs rule-yellow"></div>

  <section class="abs hero" role="img" aria-label="Photo collage of hands holding car keys and a driver at the wheel, tinted yellow"></section>
  <svg class="abs hero-check" width="96" height="96" viewBox="0 0 96 96" aria-hidden="true">
    <circle cx="48" cy="48" r="47" fill="#c9ae0d"/>
    <path d="M22 50 L40 66 L74 30" fill="none" stroke="#2a2305" stroke-width="7" stroke-linecap="square"/>
  </svg>
  <h1 class="abs hero-title">SUCCESS</h1>
  <div class="abs hero-frame"><div class="hero-frame-inner">VIEW YOUR CREDIT SCORE AND PREQUALIFICATION AMOUNT</div></div>
  <div class="abs rule-dark"></div>

  <section class="abs panel"></section>

  <div class="abs amount-tab">UP TO $75,000 PRE-QUALIFIED AMOUNT</div>
  <div class="abs congrats-box">
    <h2 class="congrats-title">CONGRATULATIONS!</h2>
    <p class="congrats-sub">You pre-qualify for <strong>UP TO $75,000</strong></p>
  </div>
  <svg class="abs badge" width="72" height="100" viewBox="0 0 72 100" aria-hidden="true">
    <path d="M16 60 L6 92 L18 86 L24 98 L32 66 Z" fill="#fcd600"/>
    <path d="M56 60 L66 92 L54 86 L48 98 L40 66 Z" fill="#fcd600"/>
    <polygon points="36,2 44,10 55,8 58,19 68,24 64,34 68,44 58,49 55,60 44,58 36,66 28,58 17,60 14,49 4,44 8,34 4,24 14,19 17,8 28,10" fill="#fcd600"/>
    <circle cx="36" cy="34" r="20" fill="none" stroke="#005469" stroke-width="4"/>
    <circle cx="36" cy="34" r="16" fill="#fcd600"/>
  </svg>

  <p class="abs dealer-note">The dealer will contact you shortly, or …</p>
  <p class="abs step-lead">You can <span>TAKE THE</span></p>
  <p class="abs step-title">NEXT STEP</p>
  <ol class="abs step-list">
    <li><span class="num">1.</span><span>Call ABC Dealer at 303-555-0142</span></li>
    <li><span class="num">2.</span><span>Email them by <u>Clicking Here</u></span></li>
    <li><span class="num">3.</span><span>Print this page and take it to<br>ABC Dealer</span></li>
  </ol>

  <a class="abs btn btn-print">
    <svg width="12" height="15" viewBox="0 0 14 16" aria-hidden="true"><path d="M0 0 H9 L14 5 V16 H0 Z" fill="#0f2b33"/></svg>
    PRINTABLE VERSION
  </a>
  <a class="abs btn btn-map">
    <svg width="18" height="17" viewBox="0 0 18 17" aria-hidden="true"><path d="M9 0 C5.5 0 3.5 2.5 3.5 5.2 C3.5 8.5 9 13 9 13 C9 13 14.5 8.5 14.5 5.2 C14.5 2.5 12.5 0 9 0 Z" fill="#0f2b33"/><circle cx="9" cy="5.2" r="2" fill="#fcd600"/><path d="M0 17 L3 11 H6 L9 14 L12 11 H15 L18 17 Z" fill="#0f2b33"/></svg>
    MAP TO DEALER
  </a>

  <p class="abs limited">YOUR PRE-QUALIFICATION IS VALID FOR A LIMITED TIME</p>
  <p class="abs act-now">ACT NOW!</p>

  <div class="abs rating-pill">tallymark rating</div>
  <div class="abs score-pill">
    <div class="score-num">703</div>
    <div class="score-label">* Your Tallymark<br>Rating 3.0</div>
  </div>
  <svg class="abs gauge" width="180" height="180" viewBox="-90 -90 180 180" aria-label="Score gauge from 300 to 850 showing 703">
    <circle r="89" fill="#0aa6cd"/>
    <circle r="72" fill="#ffffff"/>
    <path d="M -31.1 27.1 A 41.2 41.2 0 1 1 31.1 27.1" fill="none" stroke="#d3ecf3" stroke-width="14"/>
    <path d="M -31.1 27.1 A 41.2 41.2 0 1 1 36.7 -18.7" fill="none" stroke="#0aa6cd" stroke-width="14" stroke-linecap="round"/>
    <circle r="19" fill="#0aa6cd"/>
    <text x="-28" y="51" font-family="Montserrat,sans-serif" font-weight="700" font-size="8" fill="#0aa6cd" text-anchor="middle">300</text>
    <text x="29" y="51" font-family="Montserrat,sans-serif" font-weight="700" font-size="8" fill="#0aa6cd" text-anchor="middle">850</text>
  </svg>

  <div class="abs fineprint">
    <p>Your tallymark rating 3.0 is provided for educational purposes and may differ from the score a lender uses. Pre-qualification is not a loan approval, and final terms depend on verification of income, identity and the vehicle you select at the dealer. Checking your offer does not affect your credit.</p>
    <p>The amount shown is the highest you may borrow based on the information submitted today. Rates, down payment and loan length are set by the lender and the dealer. Bring a valid driver license, proof of income and proof of address when you visit to complete your purchase.</p>
    <p>Offers expire after the stated period and may change without notice. Your personal data is protected and shared only with the selected dealer and its lending partners.</p>
  </div>

  <footer class="abs footer"></footer>
  <div class="abs brand-name footer-swift">swift4lending</div>
  <div class="abs footer-powered">Powered by:</div>
  <div class="abs brand-name footer-crest">CrestLedger</div>
  <div class="abs brand-name footer-tally"><i></i>tallymark rating</div>

  <a class="abs chat">
    <div class="chat-inner">
      <svg width="24" height="20" viewBox="0 0 24 20" aria-hidden="true"><path d="M3 2 H18 A3 3 0 0 1 21 5 V12 A3 3 0 0 1 18 15 H9 L4 19 V15 H3 A3 3 0 0 1 0 12 V5 A3 3 0 0 1 3 2 Z" fill="#ffffff"/><circle cx="6" cy="8.5" r="1.4" fill="#0aa6cd"/><circle cx="10.5" cy="8.5" r="1.4" fill="#0aa6cd"/><circle cx="15" cy="8.5" r="1.4" fill="#0aa6cd"/></svg>
      <span>CHAT</span>
    </div>
  </a>
</main>
</body>
</html>
```